Looking for an amazing business card for a thriving DJ business

We need a business card design for a DJ company based in South Florida. The DJ company specializes in weddings, parties, bar mitzvahs, corporate events, proms, and reunions. We are looking for a modern, simple business card design. The card should state DJ Marlow K.
Updates

The name on the card should be DJ Marlow K

Industry/Entity Type

Entertainment Industry

Contact Information for Business Card

DJ Marlow K
415.282.6047
bxdjmarlowk@quillmail.example
https://www.facebook-example.net/DjMarlowK/
https://www.photogram-example.net/djmarlow.k/
www.djmarlowk.example

Font styles to use
Serif
Sans Serif

Requirements
Must have
• My business card has to be awesome.
Should not have
• The card has to have personality.

```html
<!DOCTYPE html>
<html lang="en">
<head>
<meta charset="utf-8">
<title>DJ Marlow K — Business Card</title>
<link rel="stylesheet" href="https://fonts.googleapis.com/css2?family=Roboto:wght@300;400&display=swap">
<style>
  :root {
    --stage: #e9e7e3;
    --card-dark: #5a5c5c;
    --card-light: #ffffff;
    --gold: #b3974a;
    --edge: #b89a4c;
    --ink: #555758;
    --rule: #6d6f70;
    --badge-ring: #d8cfb4;
  }
  * { margin: 0; padding: 0; box-sizing: border-box; }
  html, body { width: 1200px; height: 985px; overflow: hidden; }
  body {
    background: var(--stage);
    font-family: "Roboto", sans-serif;
    color: var(--ink);
    position: relative;
  }
  .card {
    position: absolute;
    left: 280px;
    width: 640px;
    height: 366px;
    border-bottom: 4px solid var(--edge);
    border-left: 3px solid var(--edge);
    box-shadow: 0 6px 18px rgba(0,0,0,0.18);
  }
  .card--back { top: 90px; background: var(--card-dark); }
  .card--front { top: 520px; background: var(--card-light); }

  .badge {
    position: absolute;
    border-radius: 50%;
    background: #fff;
    display: flex;
    align-items: center;
    justify-content: center;
    font-weight: 400;
    color: var(--ink);
    letter-spacing: 0.04em;
  }
  .card--back .badge {
    width: 220px; height: 220px;
    left: 210px; top: 73px;
    font-size: 30px;
    border: 2px solid var(--badge-ring);
  }
  .card--front .badge {
    width: 150px; height: 150px;
    left: 46px; top: 18px;
    font-size: 21px;
    border: 1.5px solid var(--ink);
  }

  .name {
    position: absolute;
    left: 44px; top: 186px;
    font-weight: 300;
    font-size: 34px;
    color: var(--gold);
    letter-spacing: 0.03em;
  }
  .rule { position: absolute; height: 1px; background: var(--rule); }
  .rule--name { left: 40px; top: 232px; width: 370px; }
  .rule--social { left: 370px; top: 282px; width: 230px; }

  .contacts {
    position: absolute;
    left: 44px; top: 246px;
    list-style: none;
    font-size: 17px;
    font-weight: 300;
  }
  .contacts li { display: flex; align-items: center; gap: 12px; height: 28px; }
  .contacts svg { width: 16px; height: 16px; flex: none; }
  .accent { color: var(--gold); }

  .social {
    position: absolute;
    right: 40px; top: 292px;
    list-style: none;
    font-size: 18px;
    font-weight: 300;
  }
  .social li { display: flex; align-items: center; gap: 10px; height: 30px; }
  .social .mark { width: 15px; height: 15px; border: 1.6px solid var(--gold); flex: none; }
  .social .mark--round { border-radius: 50%; }
</style>
</head>
<body>
  <section class="card card--back" aria-label="Card back">
    <div class="badge">Soundwell</div>
  </section>

  <section class="card card--front" aria-label="Card front">
    <div class="badge">Soundwell</div>
    <h1 class="name">DJ Marlow K</h1>
    <div class="rule rule--name"></div>
    <ul class="contacts">
      <li>
        <svg viewBox="0 0 16 16" aria-hidden="true"><path d="M4 1.5 6 5 4.6 6.4a8 8 0 0 0 5 5L11 10l3.5 2-1 2.5C7.5 14.5 1.5 8.5 1.5 2.5Z" fill="none" stroke="var(--gold)" stroke-width="1.4" stroke-linejoin="round"/></svg>
        <span>415.282.6047</span>
      </li>
      <li>
        <svg viewBox="0 0 16 16" aria-hidden="true"><rect x="1.5" y="3.5" width="13" height="9" fill="none" stroke="var(--gold)" stroke-width="1.3"/><path d="M1.5 3.5 8 9l6.5-5.5" fill="none" stroke="var(--gold)" stroke-width="1.3"/></svg>
        <span>bxdjmarlowk@quillmail.example</span>
      </li>
      <li>
        <svg viewBox="0 0 16 16" aria-hidden="true"><circle cx="8" cy="8" r="6.5" fill="none" stroke="var(--gold)" stroke-width="1.3"/><ellipse cx="8" cy="8" rx="2.8" ry="6.5" fill="none" stroke="var(--gold)" stroke-width="1.1"/><path d="M1.5 8h13" stroke="var(--gold)" stroke-width="1.1"/></svg>
        <span>www.<span class="accent">djmarlowk</span>.example</span>
      </li>
    </ul>
    <div class="rule rule--social"></div>
    <ul class="social">
      <li><span class="mark"></span><span>DjMarlowK/</span></li>
      <li><span class="mark mark--round"></span><span>djmarlow.k/</span></li>
    </ul>
  </section>
</body>
</html>
```